A4 Single Sided Brochure Folder Design Technical Company

We are a technical company based in the UK, working worldwide for Power Distribution companies.

We have technical literature and need a folder to present these in. The design should be very simple and clean using our logo and "Innovative Utility Solutions"

Our website brenvox.com gives and idea of the business but don't follow the look of the website as we will be redoing shortly.

Requirements
Must have
• Logo and Strap Line
Nice to have
• Clean, easy to print and timeless
Should not have
• Shouldn't be fashionable, we certainly aren't

```html
<!DOCTYPE html>
<html lang="en">
<head>
<meta charset="utf-8">
<title>Brenvox Presentation Folder</title>
<link rel="stylesheet" href="https://fonts.googleapis.com/css2?family=Montserrat:wght@300;400;600&display=swap">
<style>
  :root {
    --backdrop: #dcdcdc;
    --paper: #ffffff;
    --magenta: #b8288f;
    --magenta-light: #cf6cae;
    --band-text: #ffffff;
    --fold-line: #e6e6e6;
  }
  * { box-sizing: border-box; margin: 0; padding: 0; }
  html, body {
    width: 1200px;
    height: 750px;
    overflow: hidden;
    background: var(--backdrop);
    font-family: "Montserrat", sans-serif;
  }
  .folder-spread {
    position: absolute;
    left: 176px;
    top: 75px;
    width: 848px;
    height: 600px;
    display: flex;
    box-shadow: 0 10px 30px rgba(0,0,0,0.18);
  }
  .panel {
    position: relative;
    width: 424px;
    height: 600px;
    background: var(--paper);
  }
  .panel--back { border-right: 1px solid var(--fold-line); }
  .brand-band {
    position: absolute;
    left: 0;
    right: 0;
    bottom: 18px;
    height: 40px;
    background: linear-gradient(90deg, var(--magenta) 0%, var(--magenta-light) 50%, var(--magenta) 100%);
    display: flex;
    align-items: center;
  }
  .web-address {
    padding-left: 22px;
    font-size: 10px;
    font-weight: 600;
    color: var(--band-text);
  }
  .strapline {
    width: 100%;
    text-align: right;
    padding-right: 22px;
    font-size: 19px;
    font-weight: 300;
    color: var(--band-text);
    letter-spacing: 0.3px;
  }
  .brand-name {
    position: absolute;
    right: 34px;
    bottom: 66px;
    font-size: 42px;
    font-weight: 300;
    color: var(--magenta);
    line-height: 1;
  }
</style>
</head>
<body>
  <main class="folder-spread">
    <section class="panel panel--back">
      <div class="brand-band">
        <span class="web-address">www.brenvox.com</span>
      </div>
    </section>
    <section class="panel panel--front">
      <div class="brand-name">Brenvox</div>
      <div class="brand-band">
        <span class="strapline">Innovative Utility Solutions</span>
      </div>
    </section>
  </main>
</body>
</html>
```